Derek Hollins Business card

Hey there, I’m hoping to have a business card designed. I’m in Real estate and just switched to a new Brokerage called: The Property Quarter

The back could just be the company name maybe or whatever looks good!

I’ve attached some logos of our company and some cards my buddy had done up.

On the card:
Derek Hollins
derekhollins@mailbox-demo.com
587-214-6093
derekhollins-demo.ca

Target Market(s)

Home buyers and sellers

Industry/Entity Type

Real Estate

Contact Information for Business Card

just looking for a cool and modern design with my picture on it. I like the idea of Black and red being used.

Requirements
Must have
• all the details provided. I'm open to anything. Just want a professional looking card.

```html
<!DOCTYPE html>
<html lang="en">
<head>
<meta charset="UTF-8">
<title>Derek Hollins – Business Card</title>
<link href="https://fonts.googleapis.com/css2?family=Montserrat:wght@400;500;700;800&display=swap" rel="stylesheet">
<style>
  :root {
    --canvas: #e9e8ea;
    --paper: #ffffff;
    --ink: #0b0c0e;
    --red: #d21f35;
    --text: #1a1a1a;
    --photo-light: #c9ccd2;
    --photo-dark: #2b3038;
  }
  html, body {
    margin: 0;
    padding: 0;
    width: 1200px;
    height: 1108px;
    overflow: hidden;
    background: var(--canvas);
    font-family: "Montserrat", sans-serif;
  }
  .canvas {
    position: relative;
    width: 1200px;
    height: 1108px;
  }
  .card {
    position: absolute;
    overflow: hidden;
  }
  .card--front {
    left: 240px;
    top: 62px;
    width: 750px;
    height: 458px;
    background: var(--paper);
  }
  .card--back {
    left: 239px;
    top: 589px;
    width: 752px;
    height: 441px;
    background: var(--ink);
    display: flex;
    align-items: center;
    justify-content: center;
  }
  .brand-name {
    margin: 0;
    font-weight: 800;
    font-size: 58px;
    line-height: 0.98;
    letter-spacing: -1px;
    text-transform: uppercase;
  }
  .card--front .brand-name {
    position: absolute;
    left: 20px;
    top: 38px;
    color: var(--ink);
  }
  .card--back .brand-name {
    color: #ffffff;
    text-align: left;
  }
  .identity {
    position: absolute;
    left: 33px;
    top: 242px;
  }
  .identity__name {
    margin: 0;
    color: var(--red);
    font-weight: 700;
    font-size: 27px;
    line-height: 1.1;
  }
  .identity__role {
    margin: 4px 0 0;
    color: var(--text);
    font-weight: 500;
    font-size: 16px;
  }
  .contact {
    position: absolute;
    left: 32px;
    top: 328px;
    margin: 0;
    padding: 0;
    list-style: none;
  }
  .contact__item {
    display: flex;
    align-items: center;
    gap: 11px;
    height: 33px;
    color: var(--text);
    font-size: 16px;
    font-weight: 400;
  }
  .contact__icon {
    width: 17px;
    height: 17px;
    fill: var(--red);
    flex: none;
  }
  .portrait {
    position: absolute;
    left: 480px;
    top: 58px;
    width: 262px;
    height: 400px;
    background: linear-gradient(180deg, var(--photo-light) 0%, var(--photo-dark) 45%, var(--photo-dark) 100%);
    border-radius: 110px 110px 0 0;
  }
</style>
</head>
<body>
<main class="canvas">

  <section class="card card--front" aria-label="Business card front">
    <h1 class="brand-name">The Property<br>Quarter</h1>

    <div class="identity">
      <p class="identity__name">Derek Hollins</p>
      <p class="identity__role">Owner</p>
    </div>

    <ul class="contact">
      <li class="contact__item">
        <svg class="contact__icon" viewBox="0 0 24 24" aria-hidden="true"><path d="M6.6 10.8a15.1 15.1 0 0 0 6.6 6.6l2.2-2.2a1 1 0 0 1 1-.25 11.4 11.4 0 0 0 3.6.57 1 1 0 0 1 1 1V20a1 1 0 0 1-1 1A17 17 0 0 1 3 4a1 1 0 0 1 1-1h3.5a1 1 0 0 1 1 1c0 1.25.2 2.45.57 3.57a1 1 0 0 1-.25 1z"/></svg>
        587-214-6093
      </li>
      <li class="contact__item">
        <svg class="contact__icon" viewBox="0 0 24 24" aria-hidden="true"><path d="M3 5h18a1 1 0 0 1 1 1v.4l-10 6.2L2 6.4V6a1 1 0 0 1 1-1zm-1 3.7 10 6.2 10-6.2V18a1 1 0 0 1-1 1H3a1 1 0 0 1-1-1z"/></svg>
        derekhollins@mailbox-demo.com
      </li>
      <li class="contact__item">
        <svg class="contact__icon" viewBox="0 0 24 24" aria-hidden="true"><path d="M12 2a10 10 0 1 0 0 20 10 10 0 0 0 0-20zm-1 17.9A8 8 0 0 1 4.1 10L9 15v1a2 2 0 0 0 2 2zm6.9-2.5A2 2 0 0 0 16 16h-1v-3a1 1 0 0 0-1-1H8v-2h2a1 1 0 0 0 1-1V7h2a2 2 0 0 0 2-2v-.4a8 8 0 0 1 2.9 12.8z"/></svg>
        www.derekhollins-demo.ca
      </li>
    </ul>

    <div class="portrait" role="img" aria-label="Portrait photo of Derek Hollins seated in a dark suit and white shirt"></div>
  </section>

  <section class="card card--back" aria-label="Business card back">
    <p class="brand-name">The Property<br>Quarter</p>
  </section>

</main>
</body>
</html>
```